Menu Cards - Bar & Restaurant

We're a casual college sports bar in Madison, WI. We're looking for simple & creative design for menu cards that are double sided. The first card is to identify our wing sauces on the front side with our tap list on the back. The second card is for our taco night and again our tap list on the back. The font used in our logo is Air Conditioner, but I don't want this to be limiting.
Target Market(s)
18-25 college kids
Industry/Entity Type
College

```html
<!DOCTYPE html>
<html lang="en">
<head>
<meta charset="utf-8">
<title>Rebound Bar &amp; Grille – Wing Sauces</title>
<link href="https://fonts.googleapis.com/css2?family=Fredoka:wght@500;600&display=swap" rel="stylesheet">
<style>
  :root {
    --card-red: #ec2330;
    --heat-dot: #a51f2d;
    --tube-core: #a51f2d;
    --logo-dark: #2b2a2b;
    --white: #ffffff;
    --pepper-light: #e8333b;
    --pepper-deep: #9e1a22;
  }
  * { margin: 0; padding: 0; box-sizing: border-box; }
  html, body { width: 929px; height: 1200px; overflow: hidden; }
  body { background: var(--card-red); font-family: "Fredoka", sans-serif; }

  .menu-card { position: relative; width: 929px; height: 1200px; background: var(--card-red); overflow: hidden; }

  .brand-badge {
    position: absolute; left: 325px; top: 26px;
    width: 284px; height: 284px; border-radius: 50%;
    background: var(--logo-dark);
    display: flex; align-items: center; justify-content: center;
    text-align: center;
  }
  .brand-name {
    color: var(--white); font-weight: 500; font-size: 34px; line-height: 1.1;
  }

  .pepper-art {
    position: absolute; left: 168px; top: 720px;
    width: 90px; height: 430px;
    border-radius: 45px 45px 40px 40px / 120px 120px 200px 200px;
    background: linear-gradient(160deg, var(--pepper-light) 0%, var(--pepper-deep) 100%);
  }

  .thermometer { position: absolute; left: 0; top: 0; }

  .sheet-title {
    position: absolute; left: 322px; top: 332px;
    color: var(--white); font-weight: 600; font-size: 96px;
    line-height: 80px; letter-spacing: 1px;
  }
  .sheet-title .line-one { display: block; padding-left: 53px; }

  .sauce-list { position: absolute; left: 330px; top: 535px; list-style: none; }
  .sauce {
    display: flex; align-items: center;
    height: 63.7px;
    color: var(--white); font-weight: 600; font-size: 31px;
  }
  .heat { display: flex; gap: 10px; margin-left: 14px; }
  .heat i { display: block; width: 17px; height: 17px; border-radius: 50%; background: var(--heat-dot); }
</style>
</head>
<body>
<main class="menu-card">
  <div class="brand-badge">
    <span class="brand-name">Rebound<br>Bar &amp; Grille</span>
  </div>

  <div class="pepper-art" role="img" aria-label="Two red chili peppers beside the thermometer"></div>

  <svg class="thermometer" width="929" height="1200" viewBox="0 0 929 1200" aria-hidden="true">
    <rect x="254" y="380" width="30" height="745" fill="var(--white)"/>
    <circle cx="269" cy="380" r="40" fill="var(--white)"/>
    <circle cx="269" cy="380" r="19" fill="var(--card-red)"/>
    <circle cx="269" cy="1125" r="30" fill="var(--white)"/>
    <rect x="264" y="405" width="10" height="720" fill="var(--tube-core)"/>
    <circle cx="269" cy="1125" r="13" fill="var(--tube-core)"/>
  </svg>

  <h1 class="sheet-title"><span class="line-one">WING</span>SAUCES</h1>

  <ul class="sauce-list">
    <li class="sauce">Chesapeake Butter<span class="heat"><i></i></span></li>
    <li class="sauce">Honey BBQ<span class="heat"><i></i></span></li>
    <li class="sauce">Spicy Garlic<span class="heat"><i></i><i></i></span></li>
    <li class="sauce">Sweet Chili<span class="heat"><i></i><i></i></span></li>
    <li class="sauce">Jamaican Jerk<span class="heat"><i></i><i></i><i></i></span></li>
    <li class="sauce">Spicy Buffalo<span class="heat"><i></i><i></i><i></i></span></li>
    <li class="sauce">Ranch Buffalo<span class="heat"><i></i><i></i><i></i><i></i></span></li>
    <li class="sauce">Thai Peanut<span class="heat"><i></i><i></i><i></i><i></i></span></li>
    <li class="sauce">Spicy Tequila Lime<span class="heat"><i></i><i></i><i></i><i></i><i></i></span></li>
    <li class="sauce">Thermo-Nuke<span class="heat"><i></i><i></i><i></i><i></i><i></i></span></li>
  </ul>
</main>
</body>
</html>
```